Brickline Kit - iPhone app for tradespeople - UI design

Brickline Kit is an iPhone app for tradespeople (builders, carpenters, electricians, etc) which provides a range of tools that will assist with typical tasks, such as the calculation of unit conversion and spatial/volumetric/electrical measurements. The application also makes use of instruments available in the smartphone device to provide useful tools such as a spirit level, compass and torch.

The product is a simple menu-based application consisting of a number of menu and function screens. Each menu item will navigate the user to the function screen applicable to that menu item. Each function screen will contain the necessary inputs and features for perform its stated function.

The user interface should be designed with the tradesperson user in mind and as such should be simple, intuitive and durable with respect to its usability, interface design and branding elements.

Target Market(s)

Tradespeople (builders, carpenters, electricians, etc)

Industry/Entity Type

Trade

Font styles to use
Sans Serif

Requirements
Must have
• Refer to attached wireframes document...
• - Simple design
• - Consistent layout and theme
• - Screens and icons
Should not have
• - Tacky 3D images and textured backgrounds

```html
<!DOCTYPE html>
<html lang="en">
<head>
<meta charset="utf-8">
<title>Brickline Kit – Unit Conversion</title>
<link href="https://fonts.googleapis.com/css2?family=Open+Sans:wght@300;400;600&family=Arimo:wght@400&display=swap" rel="stylesheet">
<style>
  :root {
    --page-bg: #eef0f3;
    --brand-blue: #4aa0dc;
    --screen-bg: #ffffff;
    --pill-bg: #f1eff7;
    --pill-border: #d9d7e2;
    --text-dark: #333438;
    --ruler-grey: #9c9da1;
    --kb-bg: #d2d5db;
    --key-bg: #ffffff;
    --key-shadow: #898c92;
    --key-special: #adb3bc;
    --key-text: #111111;
  }
  * { box-sizing: border-box; margin: 0; padding: 0; }
  html, body { width: 1200px; height: 1000px; overflow: hidden; }
  body {
    background: var(--page-bg);
    font-family: "Open Sans", sans-serif;
    color: var(--text-dark);
    position: relative;
  }
  .screen {
    position: absolute;
    left: 330px; top: 20px;
    width: 540px; height: 960px;
    background: var(--screen-bg);
    overflow: hidden;
    box-shadow: 0 2px 14px rgba(0,0,0,0.08);
  }

  /* status bar */
  .status-bar {
    height: 34px;
    background: var(--brand-blue);
    color: #fff;
    font-size: 17px;
    display: flex; align-items: center;
    padding: 0 10px;
    position: relative;
  }
  .status-bar .carrier { display: flex; align-items: center; gap: 6px; }
  .status-bar .time { position: absolute; left: 0; right: 0; text-align: center; pointer-events: none; }
  .status-bar .battery { margin-left: auto; display: flex; align-items: center; gap: 6px; }

  /* app header */
  .app-header {
    height: 74px;
    background: var(--brand-blue);
    color: #fff;
    display: flex; align-items: center; justify-content: center;
    position: relative;
  }
  .app-header h1 { font-weight: 400; font-size: 28px; letter-spacing: 0.2px; }
  .app-header .back { position: absolute; left: 22px; top: 25px; }
  .app-header .help { position: absolute; right: 22px; top: 22px; }

  /* converter */
  .page-title {
    position: absolute; top: 135px; left: 0; right: 0;
    text-align: center;
    font-weight: 300; font-size: 38px;
  }
  .pill {
    position: absolute;
    height: 51px;
    background: var(--pill-bg);
    border: 1.5px solid var(--pill-border);
    border-radius: 26px;
    font-size: 22px;
    display: flex; align-items: center; justify-content: center;
  }
  .value-from { left: 25px; top: 229px; width: 229px; }
  .value-to { left: 286px; top: 229px; width: 229px; }
  .equals {
    position: absolute; left: 254px; width: 32px; top: 229px; height: 51px;
    display: flex; align-items: center; justify-content: center;
    font-size: 30px; color: var(--text-dark);
  }
  .unit-select { left: 25px; top: 292px; width: 490px; height: 50px; justify-content: flex-start; }
  .unit-select .unit { width: 50%; text-align: center; }
  .unit-select .unit-from { padding-right: 22px; }
  .unit-select .unit-to { padding-left: 22px; }
  .unit-toggle {
    position: absolute; left: 220px; top: -1.5px;
    width: 47px; height: 50px;
    background: var(--brand-blue);
    display: flex; align-items: center; justify-content: center;
  }

  .ruler-label {
    position: absolute; left: 0; right: 0; text-align: center;
    font-size: 21px;
  }
  .ruler-label.top { top: 382px; }
  .ruler-label.bottom { top: 434px; }
  .ruler { position: absolute; left: 41px; top: 404px; }

  /* keyboard */
  .keyboard {
    position: absolute; left: 0; right: 0; top: 594px; bottom: 0;
    background: var(--kb-bg);
    font-family: "Arimo", sans-serif;
  }
  .key-row { position: absolute; left: 0; right: 0; height: 64px; }
  .key {
    position: absolute; top: 0;
    width: 47px; height: 64px;
    background: var(--key-bg);
    border-radius: 7px;
    box-shadow: 0 2px 0 var(--key-shadow);
    display: flex; align-items: center; justify-content: center;
    font-size: 36px; color: var(--key-text);
  }
  .key.special { background: var(--key-special); }
  .key.small { font-size: 24px; }
  .row-1 { top: 21px; }
  .row-2 { top: 113px; }
  .row-3 { top: 203px; }
  .row-4 { top: 294px; }
</style>
</head>
<body>
<main class="screen">
  <div class="status-bar">
    <div class="carrier">
      <svg width="62" height="12" viewBox="0 0 62 12" aria-hidden="true">
        <g fill="#fff" stroke="#fff" stroke-width="1.2">
          <circle cx="6" cy="6" r="4.6"/><circle cx="18" cy="6" r="4.6"/><circle cx="30" cy="6" r="4.6"/>
          <circle cx="42" cy="6" r="4.2" fill="none"/><circle cx="54" cy="6" r="4.2" fill="none"/>
        </g>
      </svg>
      <span>VOLT</span>
      <svg width="22" height="16" viewBox="0 0 22 16" aria-hidden="true">
        <path d="M11 15 L7.5 11 A5 5 0 0 1 14.5 11 Z" fill="#fff"/>
        <path d="M4.5 8 A9.5 9.5 0 0 1 17.5 8" stroke="#fff" stroke-width="2.2" fill="none"/>
        <path d="M1.5 4.8 A14 14 0 0 1 20.5 4.8" stroke="#fff" stroke-width="2.2" fill="none"/>
      </svg>
    </div>
    <div class="time">11:27 AM</div>
    <div class="battery">
      <span>100%</span>
      <svg width="38" height="16" viewBox="0 0 38 16" aria-hidden="true">
        <rect x="1" y="1" width="32" height="14" rx="2.5" fill="none" stroke="#fff" stroke-width="1.5"/>
        <rect x="3" y="3" width="28" height="10" rx="1" fill="#fff"/>
        <rect x="34.5" y="5" width="2.5" height="6" rx="1" fill="#fff"/>
      </svg>
    </div>
  </div>

  <header class="app-header">
    <svg class="back" width="26" height="24" viewBox="0 0 26 24" aria-label="Back">
      <path d="M24 12 H3 M11 3 L2 12 L11 21" stroke="#fff" stroke-width="2.6" fill="none" stroke-linecap="round" stroke-linejoin="round"/>
    </svg>
    <h1>Unit Conversion</h1>
    <svg class="help" width="30" height="30" viewBox="0 0 30 30" aria-label="Help">
      <circle cx="15" cy="15" r="13" fill="none" stroke="#fff" stroke-width="2"/>
      <text x="15" y="21" text-anchor="middle" font-family="Open Sans, sans-serif" font-size="17" fill="#fff">?</text>
    </svg>
  </header>

  <h2 class="page-title">Length Conversion</h2>

  <div class="pill value-from">20</div>
  <div class="equals">=</div>
  <div class="pill value-to">7.874016</div>

  <div class="pill unit-select">
    <span class="unit unit-from">Centimeter</span>
    <span class="unit unit-to">Inches</span>
    <span class="unit-toggle">
      <svg width="20" height="12" viewBox="0 0 20 12" aria-hidden="true">
        <path d="M2 2 L10 10 L18 2" stroke="#fff" stroke-width="2" fill="none"/>
      </svg>
    </span>
  </div>

  <div class="ruler-label top">20 cm</div>
  <svg class="ruler" width="458" height="34" viewBox="0 0 458 34" aria-hidden="true">
    <g stroke="var(--ruler-grey)" stroke-width="4">
      <line x1="2" y1="0" x2="2" y2="34"/>
      <line x1="456" y1="0" x2="456" y2="34"/>
      <line x1="2" y1="17" x2="456" y2="17"/>
    </g>
  </svg>
  <div class="ruler-label bottom">7.874016 in</div>

  <section class="keyboard" aria-label="Keyboard">
    <div class="key-row row-1">
      <span class="key" style="left:7px">Q</span>
      <span class="key" style="left:60px">W</span>
      <span class="key" style="left:114px">E</span>
      <span class="key" style="left:167px">R</span>
      <span class="key" style="left:221px">T</span>
      <span class="key" style="left:274px">Y</span>
      <span class="key" style="left:328px">U</span>
      <span class="key" style="left:381px">I</span>
      <span class="key" style="left:435px">O</span>
      <span class="key" style="left:488px">P</span>
    </div>
    <div class="key-row row-2">
      <span class="key" style="left:33px">A</span>
      <span class="key" style="left:87px">S</span>
      <span class="key" style="left:140px">D</span>
      <span class="key" style="left:194px">F</span>
      <span class="key" style="left:247px">G</span>
      <span class="key" style="left:301px">H</span>
      <span class="key" style="left:354px">J</span>
      <span class="key" style="left:408px">K</span>
      <span class="key" style="left:461px">L</span>
    </div>
    <div class="key-row row-3">
      <span class="key special" style="left:6px;width:58px" aria-label="Shift">
        <svg width="26" height="26" viewBox="0 0 26 26" aria-hidden="true">
          <path d="M13 2 L24 14 H18 V24 H8 V14 H2 Z" fill="none" stroke="#222" stroke-width="1.8" stroke-linejoin="round"/>
        </svg>
      </span>
      <span class="key" style="left:88px">Z</span>
      <span class="key" style="left:142px">X</span>
      <span class="key" style="left:195px">C</span>
      <span class="key" style="left:249px">V</span>
      <span class="key" style="left:302px">B</span>
      <span class="key" style="left:356px">N</span>
      <span class="key" style="left:409px">M</span>
      <span class="key special" style="left:476px;width:58px" aria-label="Delete">
        <svg width="34" height="24" viewBox="0 0 34 24" aria-hidden="true">
          <path d="M10 2 H32 V22 H10 L1 12 Z" fill="none" stroke="#222" stroke-width="1.8" stroke-linejoin="round"/>
          <path d="M15 7 L25 17 M25 7 L15 17" stroke="#222" stroke-width="1.8"/>
        </svg>
      </span>
    </div>
    <div class="key-row row-4">
      <span class="key special small" style="left:6px;width:55px">123</span>
      <span class="key special" style="left:73px;width:55px" aria-label="Language">
        <svg width="30" height="30" viewBox="0 0 30 30" aria-hidden="true">
          <g fill="none" stroke="#222" stroke-width="1.5">
            <circle cx="15" cy="15" r="12"/>
            <ellipse cx="15" cy="15" rx="5.5" ry="12"/>
            <line x1="15" y1="3" x2="15" y2="27"/>
            <line x1="3" y1="15" x2="27" y2="15"/>
            <path d="M5 8.5 H25 M5 21.5 H25"/>
          </g>
        </svg>
      </span>
      <span class="key small" style="left:140px;width:124px">space</span>
      <span class="key small" style="left:276px;width:55px">@</span>
      <span class="key small" style="left:343px;width:57px">.</span>
      <span class="key special small" style="left:411px;width:123px">return</span>
    </div>
  </section>
</main>
</body>
</html>
```